Company Values Graphic

We are looking for a design of our company values that can be used in a variety of places including our website, mousepads, office posters, business cards, etc.

Notes:
- We'd rather have icons/art than photographs on the poster.... so more like an infographic
- The core value group headings are not required, but can be included if you think grouping the values works for your design
- We have a logo for our software product but that logo is not required
- We don't need/want clever images to accompany each value, but some images are fine
- BrisKel logo attached
- BrisKel colors are attached
- BrisKel logo is Nunito Sans ExtraBold 800
- BrisKel website uses Roboto

Our Values - Who we will work with (and who we will not)
The right set of values are essential to building and maintaining a culture that we all wake up eager to be a part of each day. They are foundational to all hiring and firing decisions. They attract the right people and repel the wrong ones.

BE HELPFUL
Make every person and place better because you are there.
Deliver wow with every interaction.

BE HUMBLE
Listen with every muscle.
Passionately help others first.
Seek first to understand.

BE HONEST
Earn trust every day.
Be open and direct.
Treat everyone with fairness and respect.

BE HUMAN
Celebrate passion and action.
Create an environment where people are authentic.
Hire great people and expect a lot from them

BE COURAGEOUS
Dare mighty things.
Make and honor commitments.
All great things start with a small act of courage applied at the right moment.

```html
<!DOCTYPE html>
<html lang="en">
<head>
<meta charset="utf-8">
<title>BrisKel — Our Values</title>
<link href="https://fonts.googleapis.com/css2?family=Montserrat:wght@800;900&family=Nunito+Sans:ital,wght@0,300;0,400;0,800;1,800;1,900&display=swap" rel="stylesheet">
<style>
  :root {
    --ink: #0d0d0d;
    --flame-orange: #f05a24;
    --flame-amber: #f7991d;
    --flame-red: #ec2227;
    --paper: #ffffff;
  }
  * { margin: 0; padding: 0; box-sizing: border-box; }
  html, body { width: 1200px; height: 1000px; overflow: hidden; background: var(--paper); }
  .poster { position: relative; width: 1200px; height: 1000px; font-family: "Nunito Sans", sans-serif; color: var(--ink); }

  .brand { position: absolute; left: 110px; top: 136px; display: flex; align-items: center; gap: 14px; }
  .brand-dot { width: 50px; height: 50px; border-radius: 50%; background: var(--flame-orange); }
  .brand-name { font-family: "Nunito Sans", sans-serif; font-weight: 800; font-size: 38px; color: var(--ink); letter-spacing: -0.5px; }

  .title { position: absolute; left: 110px; top: 193px; font-family: "Montserrat", sans-serif; font-weight: 900; font-size: 79px; line-height: 1; letter-spacing: -1.5px; }
  .subtitle { position: absolute; left: 114px; top: 280px; font-family: "Montserrat", sans-serif; font-weight: 800; font-size: 30.5px; line-height: 27px; color: var(--flame-orange); text-transform: uppercase; letter-spacing: 0.2px; }

  .intro { position: absolute; left: 114px; top: 356px; font-weight: 300; font-size: 22px; line-height: 28.5px; }
  .intro span { display: block; white-space: nowrap; }
  .intro .l1 { word-spacing: 4px; }
  .intro .l4 { word-spacing: 6px; }
  .intro .l6 { padding-left: 107px; word-spacing: 2px; }
  .intro .l7 { padding-left: 156px; word-spacing: 22px; }
  .intro .l8 { padding-left: 189px; }

  .mascot-art { position: absolute; left: 150px; top: 562px; width: 205px; height: 352px; border-radius: 90px 90px 40px 40px; background: linear-gradient(160deg, var(--flame-amber), var(--flame-orange) 55%, var(--flame-red)); opacity: 0.85; }

  .value-heading { position: absolute; transform: translate(-50%, -50%); font-weight: 900; font-style: italic; font-size: 24px; color: var(--flame-orange); white-space: nowrap; letter-spacing: 0.2px; }

  .value-band { position: absolute; width: 526px; height: 96px; }
  .value-band svg { position: absolute; inset: 0; }
  .value-text { position: absolute; left: 0; top: 0; width: 458px; height: 96px; display: flex; flex-direction: column; justify-content: center; align-items: center; text-align: center; color: var(--paper); font-size: 15px; line-height: 18.4px; font-weight: 400; }
</style>
</head>
<body>
<main class="poster">
  <svg width="0" height="0" style="position:absolute">
    <defs>
      <linearGradient id="bandFill" x1="0" x2="1" y1="0" y2="0">
        <stop offset="0" stop-color="#f7991d"/>
        <stop offset="1" stop-color="#f05a24"/>
      </linearGradient>
      <path id="bandShape" d="M48 0 H526 C478 0 462 30 442 62 C424 90 406 96 390 96 H48 A48 48 0 0 1 48 0 Z"/>
    </defs>
  </svg>

  <div class="brand"><span class="brand-dot"></span><span class="brand-name">BrisKel</span></div>
  <h1 class="title">OUR VALUE</h1>
  <h2 class="subtitle">Who we will work with<br>(and who we will not)</h2>

  <p class="intro">
    <span class="l1">The right set of values are essential to</span>
    <span class="l2">building and maintaining a culture that</span>
    <span class="l3">we all wake up eager to be a part of</span>
    <span class="l4">each day. They are foundational to</span>
    <span class="l5">all hiring and firing decisions. They</span>
    <span class="l6">attract the right people</span>
    <span class="l7">and repel the</span>
    <span class="l8">wrong ones.</span>
  </p>

  <div class="mascot-art" role="img" aria-label="Illustration of a flame-headed mascot flexing its arm"></div>

  <h3 class="value-heading" style="left:864px;top:234px">BE HELPFUL</h3>
  <div class="value-band" style="left:602px;top:260px">
    <svg viewBox="0 0 526 96"><use href="#bandShape" fill="url(#bandFill)"/></svg>
    <p class="value-text" style="left:30px">Make every person and place better<br>because you are there.<br>Deliver wow with every interaction.</p>
  </div>

  <h3 class="value-heading" style="left:810px;top:375px">BE HUMBLE</h3>
  <div class="value-band" style="left:548px;top:400px">
    <svg viewBox="0 0 526 96"><use href="#bandShape" fill="url(#bandFill)"/></svg>
    <p class="value-text" style="left:30px">Listen with every muscle.<br>Passionately help others first.<br>Seek first to understand.</p>
  </div>

  <h3 class="value-heading" style="left:755px;top:516px">BE HONEST</h3>
  <div class="value-band" style="left:493px;top:539px">
    <svg viewBox="0 0 526 96"><use href="#bandShape" fill="url(#bandFill)"/></svg>
    <p class="value-text" style="left:30px">Earn trust every day.<br>Be open and direct.<br>Treat everyone with fairness and respect.</p>
  </div>

  <h3 class="value-heading" style="left:701px;top:657px">BE HUMAN</h3>
  <div class="value-band" style="left:439px;top:678px">
    <svg viewBox="0 0 526 96"><use href="#bandShape" fill="url(#bandFill)"/></svg>
    <p class="value-text" style="left:0;width:460px">Celebrate passion and action.<br>Create an environment where people are authentic.<br>Hire great people and expect a lot from them</p>
  </div>

  <h3 class="value-heading" style="left:647px;top:798px">BE COURAGEOUS</h3>
  <div class="value-band" style="left:384px;top:818px">
    <svg viewBox="0 0 526 96"><use href="#bandShape" fill="url(#bandFill)"/></svg>
    <p class="value-text" style="left:0;width:460px">Dare mighty things.<br>Make and honor commitments.<br>All great things start with a small act of courage applied<br>at the right moment.</p>
  </div>
</main>
</body>
</html>
```